Statement of Professional Excellence

Our school community has create a statement of Professional Excellence at our school (LAM = The Linden Academy at Marbury) This will be shared internally and with candidates interviewing at our school. We'd like a branded graphic that lists in an interesting way our statements:

Professional Excellence at LAM

We honor the whole child while embracing them where they are.
We are mission-driven individuals whose dedication to our students motivates our daily work.
We bring flexible thinking to allow the needs of the students to drive the learning.
We are patient, nurturing, empathetic, and compassionate people.
We value, trust, and support each other.
We learn and we teach.
We lean into and celebrate diversity.
We build trust through genuine partnerships with families.
We are quirky, fun and proud of it.

```html
<!DOCTYPE html>
<html lang="en">
<head>
<meta charset="utf-8">
<title>Professional Excellence at LAM</title>
<link rel="stylesheet" href="https://fonts.googleapis.com/css2?family=Open+Sans:wght@400;600&display=swap">
<style>
  :root {
    --navy: #263547;
    --gold: #d4b12a;
    --slate: #4a5560;
    --text: #5b6670;
    --rule: #e3e5e8;
    --frame: #eef0f2;
    --paper: #ffffff;
  }
  * { box-sizing: border-box; margin: 0; padding: 0; }
  html, body { width: 849px; height: 1200px; overflow: hidden; background: var(--paper); }
  .sheet {
    position: relative;
    width: 849px;
    height: 1200px;
    background: var(--frame);
    font-family: "Open Sans", Arial, sans-serif;
  }
  .masthead {
    height: 268px;
    background: var(--navy);
    display: flex;
    align-items: center;
    justify-content: center;
  }
  .school-name {
    color: var(--gold);
    font-weight: 600;
    font-size: 34px;
    letter-spacing: 1px;
    text-align: center;
    line-height: 1.25;
    max-width: 460px;
  }
  .statements {
    position: absolute;
    left: 62px;
    top: 318px;
    width: 725px;
    height: 800px;
    background: var(--paper);
    list-style: none;
    padding: 6px 40px 0 40px;
  }
  .statement {
    display: flex;
    align-items: center;
    min-height: 87px;
    border-bottom: 1.5px solid var(--rule);
  }
  .statement:last-child { border-bottom: none; }
  .statement-mark { flex: 0 0 42px; width: 42px; height: 38px; margin-right: 32px; }
  .statement-text {
    color: var(--text);
    font-size: 20px;
    line-height: 1.3;
  }
  .footer-band {
    position: absolute;
    left: 0; right: 0; bottom: 0;
    height: 62px;
    background: var(--navy);
  }
  .footer-band::after {
    content: "";
    position: absolute;
    left: 0; right: 0; top: 18px;
    height: 7px;
    background: var(--gold);
  }
</style>
</head>
<body>
<div class="sheet">
  <header class="masthead">
    <div class="school-name">The Linden Academy at Marbury</div>
  </header>

  <ul class="statements">
    <li class="statement"><svg class="statement-mark" viewBox="0 0 42 38"><polygon points="0,0 14,0 28,19 14,38 0,38 14,19" fill="var(--gold)"/><polygon points="14,0 26,0 40,19 26,38 14,38 28,19" fill="var(--slate)"/></svg><span class="statement-text">We honor the whole child while embracing them where they are.</span></li>
    <li class="statement"><svg class="statement-mark" viewBox="0 0 42 38"><polygon points="0,0 14,0 28,19 14,38 0,38 14,19" fill="var(--gold)"/><polygon points="14,0 26,0 40,19 26,38 14,38 28,19" fill="var(--slate)"/></svg><span class="statement-text">We are mission-driven individuals whose dedication to our students motivates our daily work.</span></li>
    <li class="statement"><svg class="statement-mark" viewBox="0 0 42 38"><polygon points="0,0 14,0 28,19 14,38 0,38 14,19" fill="var(--gold)"/><polygon points="14,0 26,0 40,19 26,38 14,38 28,19" fill="var(--slate)"/></svg><span class="statement-text">We bring flexible thinking to allow the needs of the students to drive the learning.</span></li>
    <li class="statement"><svg class="statement-mark" viewBox="0 0 42 38"><polygon points="0,0 14,0 28,19 14,38 0,38 14,19" fill="var(--gold)"/><polygon points="14,0 26,0 40,19 26,38 14,38 28,19" fill="var(--slate)"/></svg><span class="statement-text">We are patient, nurturing, empathetic, and compassionate people.</span></li>
    <li class="statement"><svg class="statement-mark" viewBox="0 0 42 38"><polygon points="0,0 14,0 28,19 14,38 0,38 14,19" fill="var(--gold)"/><polygon points="14,0 26,0 40,19 26,38 14,38 28,19" fill="var(--slate)"/></svg><span class="statement-text">We value, trust, and support each other.</span></li>
    <li class="statement"><svg class="statement-mark" viewBox="0 0 42 38"><polygon points="0,0 14,0 28,19 14,38 0,38 14,19" fill="var(--gold)"/><polygon points="14,0 26,0 40,19 26,38 14,38 28,19" fill="var(--slate)"/></svg><span class="statement-text">We learn and we teach.</span></li>
    <li class="statement"><svg class="statement-mark" viewBox="0 0 42 38"><polygon points="0,0 14,0 28,19 14,38 0,38 14,19" fill="var(--gold)"/><polygon points="14,0 26,0 40,19 26,38 14,38 28,19" fill="var(--slate)"/></svg><span class="statement-text">We lean into and celebrate diversity.</span></li>
    <li class="statement"><svg class="statement-mark" viewBox="0 0 42 38"><polygon points="0,0 14,0 28,19 14,38 0,38 14,19" fill="var(--gold)"/><polygon points="14,0 26,0 40,19 26,38 14,38 28,19" fill="var(--slate)"/></svg><span class="statement-text">We build trust through genuine partnerships with families.</span></li>
    <li class="statement"><svg class="statement-mark" viewBox="0 0 42 38"><polygon points="0,0 14,0 28,19 14,38 0,38 14,19" fill="var(--gold)"/><polygon points="14,0 26,0 40,19 26,38 14,38 28,19" fill="var(--slate)"/></svg><span class="statement-text">We are quirky, fun and proud of it.</span></li>
  </ul>

  <footer class="footer-band"></footer>
</div>
</body>
</html>
```